Business Card Design for Online Gift Business

Business card design for a new online Canadian company called "Harlow & Reed Gift Crates" selling modern and luxurious gift boxes for every occasion. Items are sourced locally from talented socially-responsible Canadian artisans. Each gift is elegantly presented in a keepsake wood box to ensure a lasting impression.

Industry/Entity Type

E-Commerce

Contact Information for Business Card

Merin Holloway, Proprietor
Kelowna, BC
587-214-3306
www.harlowandreed.ca
hello@harlowandreed.ca

Requirements
Must have
• Made by our finest, for your finest
• Please also include the symbols for Facebook and Instagram
Nice to have
• **I have attached a few samples of background colors and font colors that I like. I hope this helps in a few directions to try.

```html
<!DOCTYPE html>
<html lang="en">
<head>
<meta charset="utf-8">
<title>Harlow &amp; Reed Gift Crates — Business Card</title>
<link rel="stylesheet" href="https://fonts.googleapis.com/css2?family=Cinzel:wght@400;500&family=Allura&display=swap">
<style>
  :root {
    --backdrop: #e7e7e7;
    --card-top: #cdc2ac;
    --card-bottom: #c3b79f;
    --brand-brown: #5b3e28;
    --ink: #2f2b28;
    --leaf-wash: rgba(236, 230, 216, 0.45);
    --card-shadow: rgba(0, 0, 0, 0.28);
  }
  * { margin: 0; padding: 0; box-sizing: border-box; }
  html, body {
    width: 1200px;
    height: 576px;
    overflow: hidden;
    background: var(--backdrop);
  }
  .sheet {
    position: relative;
    width: 1200px;
    height: 576px;
  }
  .card {
    position: absolute;
    top: 139px;
    width: 484px;
    height: 293px;
    border-radius: 8px;
    background: linear-gradient(180deg, var(--card-top), var(--card-bottom));
    box-shadow: 0 3px 6px var(--card-shadow);
    overflow: hidden;
    color: var(--ink);
    font-family: "Cinzel", "Times New Roman", serif;
    text-align: center;
  }
  .card--front { left: 82px; }
  .card--back { left: 602px; }

  /* front */
  .wordmark {
    position: absolute;
    left: 0;
    right: 0;
    top: 122px;
    font-weight: 500;
    font-size: 38px;
    line-height: 44px;
    letter-spacing: 2px;
    color: var(--brand-brown);
  }
  .tagline {
    position: absolute;
    left: 0;
    right: 0;
    top: 204px;
    font-size: 13.5px;
    line-height: 18px;
    letter-spacing: 0.4px;
    color: var(--ink);
  }

  /* back */
  .leaf-wash {
    position: absolute;
    left: 110px;
    top: 34px;
    width: 264px;
    height: 258px;
    background: radial-gradient(ellipse at 50% 50%, var(--leaf-wash) 0%, rgba(236, 230, 216, 0.2) 55%, rgba(236, 230, 216, 0) 72%);
  }
  .holder-name {
    position: absolute;
    left: 0;
    right: 0;
    top: 52px;
    font-family: "Allura", cursive;
    font-weight: 400;
    font-size: 42px;
    line-height: 46px;
    letter-spacing: 1.5px;
    color: var(--ink);
  }
  .holder-role {
    position: absolute;
    left: 0;
    right: 0;
    top: 99px;
    font-size: 11.5px;
    line-height: 14px;
    letter-spacing: 1px;
  }
  .contact-list {
    position: absolute;
    left: 0;
    right: 0;
    top: 149px;
    list-style: none;
    font-size: 12.5px;
    line-height: 18px;
  }
  .social-row {
    position: absolute;
    left: 0;
    right: 0;
    top: 223px;
    display: flex;
    justify-content: center;
    gap: 5px;
  }
  .social-mark {
    width: 11px;
    height: 11px;
    border-radius: 2px;
    background: var(--ink);
  }
</style>
</head>
<body>
  <main class="sheet">
    <section class="card card--front" aria-label="Business card front">
      <div class="wordmark">Harlow &amp; Reed</div>
      <p class="tagline">Made by our finest, for your finest</p>
    </section>

    <section class="card card--back" aria-label="Business card back">
      <div class="leaf-wash" role="img" aria-label="Faint brand emblem decoration"></div>
      <h1 class="holder-name">Merin Holloway</h1>
      <p class="holder-role">Proprietor</p>
      <ul class="contact-list">
        <li>Kelowna, BC</li>
        <li>587-214-3306</li>
        <li>www.harlowandreed.ca</li>
        <li>hello@harlowandreed.ca</li>
      </ul>
      <div class="social-row">
        <span class="social-mark" role="img" aria-label="Social profile one"></span>
        <span class="social-mark" role="img" aria-label="Social profile two"></span>
      </div>
    </section>
  </main>
</body>
</html>
```